Real Estate Open House A Frame Sign

The sign is 22" wide and 28" tall. This sign is used to post around the neighbourhood to direct people to an open house (home that is for sale). It is also used for self-promotion.

Designwise
- I just want something with a modern look, simple and clean.
- I want my picture and business logo on the left side.
- On the right side, website (www.lumwick-realestate.com) and my phone (555-374-9126), then a blank space where I can write an address when I need to.

I'm not sure how I want the overall design look. I'm very open-minded and I'm depending on your creative mind to come up with something.

If you have any questions, please let me know.

```html
<!DOCTYPE html>
<html lang="en">
<head>
<meta charset="utf-8">
<title>Open House Sign Concepts</title>
<link href="https://fonts.googleapis.com/css2?family=Abril+Fatface&family=Montserrat:wght@400;600;800&display=swap" rel="stylesheet">
<style>
  :root {
    --brand-blue: #0c4585;
    --ink: #1c1c1c;
    --charcoal: #2a2a2a;
    --paper: #ffffff;
    --edge: #c9c9c9;
    --stage-light: #4b4b4b;
    --stage-dark: #2a2a2a;
    --label: #f2f2f2;
  }
  * { box-sizing: border-box; margin: 0; padding: 0; }
  html, body { width: 1037px; height: 1200px; overflow: hidden; }
  body {
    position: relative;
    background: radial-gradient(ellipse at 50% 50%, var(--stage-light) 0%, var(--stage-dark) 75%);
    font-family: "Montserrat", Arial, sans-serif;
  }
  .sign {
    position: absolute;
    width: 384px;
    height: 487px;
    background: var(--paper);
    overflow: hidden;
    box-shadow: 0 6px 14px rgba(0,0,0,.45);
  }
  .sign::after {
    content: "";
    position: absolute;
    left: 0; right: 0; bottom: 0;
    height: 5px;
    background: var(--edge);
  }
  .sign--photo   { left: 79px;  top: 59px; }
  .sign--house   { left: 561px; top: 59px; }
  .sign--light   { left: 79px;  top: 639px; }
  .sign--dark    { left: 561px; top: 639px; }

  .label {
    position: absolute;
    width: 384px;
    text-align: center;
    color: var(--label);
    font-size: 23px;
    font-weight: 400;
    letter-spacing: .5px;
  }

  .scene-photo {
    position: absolute; left: 0; top: 0; width: 100%; height: 282px;
    background: linear-gradient(160deg, #24311f 0%, #3d3a2c 35%, #5a4434 55%, #2b3624 80%, #1f2a1c 100%);
  }
  .dark-field {
    position: absolute; left: 0; top: 0; width: 100%; height: 250px;
    background: var(--charcoal);
  }
  .house-field {
    position: absolute; left: 0; top: 0; width: 100%; height: 336px;
    background: var(--brand-blue);
  }

  .headline {
    position: absolute; left: 0; width: 100%;
    text-align: center;
    font-family: "Abril Fatface", "Bodoni Moda", serif;
    font-weight: 400;
    line-height: .88;
  }
  .headline span { display: block; }
  .headline--script { top: 22px; color: var(--paper); font-size: 104px; letter-spacing: -1px; }
  .headline--caps { font-size: 88px; }
  .headline--caps .line-1 { letter-spacing: 5px; padding-left: 5px; }
  .headline--caps .line-2 { margin-top: 12px; font-size: 94px; letter-spacing: 3px; padding-left: 3px; }
  .sign--house .headline--caps { top: 70px; color: var(--paper); font-size: 80px; }
  .sign--house .headline--caps .line-1 { letter-spacing: 7px; padding-left: 7px; }
  .sign--house .headline--caps .line-2 { margin-top: 8px; font-size: 86px; letter-spacing: 3px; padding-left: 3px; }
  .sign--light .headline--caps { top: 32px; }
  .sign--light .line-1 { color: var(--brand-blue); }
  .sign--light .line-2 { color: var(--ink); }
  .sign--dark .headline--caps { top: 32px; color: var(--paper); }

  .band {
    position: absolute; left: 0; width: 100%;
    background: var(--brand-blue);
  }
  .sign--photo .band { top: 281px; height: 86px; }
  .sign--light .band,
  .sign--dark .band  { top: 250px; height: 86px; }

  .brand {
    position: absolute;
    color: var(--paper);
    font-weight: 400;
    line-height: 1;
  }
  .brand-name { display: block; font-size: 38px; letter-spacing: 2px; }
  .brand-tag { display: block; margin-top: 8px; font-size: 14px; letter-spacing: 9.4px; }
  .sign--photo .brand { left: 29px; top: 296px; }
  .sign--light .brand,
  .sign--dark .brand { left: 29px; top: 265px; }
  .sign--house .brand { left: 0; width: 100%; top: 256px; text-align: center; }
  .sign--house .brand-tag { padding-left: 9px; }

  .portrait {
    position: absolute;
    background: linear-gradient(180deg, #c4c4c4 0%, #a9a9a9 45%, #3b4047 75%, #2c3038 100%);
    border: 3px solid #b8b8b8;
  }
  .sign--photo .portrait { left: 244px; top: 219px; width: 125px; height: 148px; border-color: #5b5b5b; }
  .sign--light .portrait { left: 246px; top: 221px; width: 121px; height: 145px; }
  .sign--dark .portrait  { left: 246px; top: 221px; width: 121px; height: 145px; border-color: #5b5b5b; }
  .sign--house .portrait { left: 265px; top: 340px; width: 115px; height: 138px; border-color: #e0e0e0; }

  .contact {
    position: absolute;
    color: var(--brand-blue);
    font-weight: 800;
  }
  .contact-row { display: flex; align-items: center; }
  .contact-row svg { flex: none; margin-right: 9px; }
  .phone { font-size: 38px; letter-spacing: -.5px; line-height: 1.05; }
  .web { font-size: 16px; margin-top: 1px; }
  .sign--photo .contact { left: 38px; top: 382px; }
  .sign--light .contact,
  .sign--dark .contact { left: 38px; top: 362px; }
  .sign--house .contact { left: 18px; top: 350px; }
  .sign--house .phone { font-size: 35px; }
  .sign--house .web { font-size: 14.3px; margin-top: 4px; }
</style>
</head>
<body>

  <section class="sign sign--photo">
    <div class="scene-photo" role="img" aria-label="Softly blurred photo of a home and garden"></div>
    <h2 class="headline headline--script"><span>Open</span><span>House</span></h2>
    <div class="band"></div>
    <div class="brand"><span class="brand-name">LUMWICK</span><span class="brand-tag">REAL ESTATE</span></div>
    <div class="portrait" role="img" aria-label="Portrait photo of the agent"></div>
    <div class="contact">
      <div class="contact-row phone">
        <svg width="26" height="26" viewBox="0 0 26 26" aria-hidden="true"><circle cx="13" cy="13" r="13" fill="var(--brand-blue)"/><path d="M11 6c-2 1-3 3-3 7s1 6 3 7l2-3-2-2c-.4-1-.4-3 0-4l2-2z" fill="#fff"/></svg>
        <span>555-374-9126</span>
      </div>
      <div class="contact-row web">
        <svg width="24" height="22" viewBox="0 0 24 22" aria-hidden="true"><g fill="none" stroke="var(--brand-blue)" stroke-width="1.6"><circle cx="10" cy="10" r="8.5"/><ellipse cx="10" cy="10" rx="3.8" ry="8.5"/><path d="M1.5 10h17M3 5.5h14M3 14.5h14"/></g><path d="M15 13l7 3-3 1 2 3-1.5 1-2-3-2 2z" fill="var(--brand-blue)"/></svg>
        <span>www.lumwick-realestate.com</span>
      </div>
    </div>
  </section>

  <section class="sign sign--house">
    <div class="house-field" role="img" aria-label="House silhouette graphic in brand blue"></div>
    <h2 class="headline headline--caps"><span class="line-1">OPEN</span><span class="line-2">HOUSE</span></h2>
    <div class="brand"><span class="brand-name">LUMWICK</span><span class="brand-tag">REAL ESTATE</span></div>
    <div class="contact">
      <div class="phone">555-374-9126</div>
      <div class="web">www.lumwick-realestate.com</div>
    </div>
    <div class="portrait" role="img" aria-label="Portrait photo of the agent"></div>
  </section>

  <section class="sign sign--light">
    <h2 class="headline headline--caps"><span class="line-1">OPEN</span><span class="line-2">HOUSE</span></h2>
    <div class="band"></div>
    <div class="brand"><span class="brand-name">LUMWICK</span><span class="brand-tag">REAL ESTATE</span></div>
    <div class="portrait" role="img" aria-label="Portrait photo of the agent"></div>
    <div class="contact">
      <div class="contact-row phone">
        <svg width="26" height="26" viewBox="0 0 26 26" aria-hidden="true"><circle cx="13" cy="13" r="13" fill="var(--brand-blue)"/><path d="M11 6c-2 1-3 3-3 7s1 6 3 7l2-3-2-2c-.4-1-.4-3 0-4l2-2z" fill="#fff"/></svg>
        <span>555-374-9126</span>
      </div>
      <div class="contact-row web">
        <svg width="24" height="22" viewBox="0 0 24 22" aria-hidden="true"><g fill="none" stroke="var(--brand-blue)" stroke-width="1.6"><circle cx="10" cy="10" r="8.5"/><ellipse cx="10" cy="10" rx="3.8" ry="8.5"/><path d="M1.5 10h17M3 5.5h14M3 14.5h14"/></g><path d="M15 13l7 3-3 1 2 3-1.5 1-2-3-2 2z" fill="var(--brand-blue)"/></svg>
        <span>www.lumwick-realestate.com</span>
      </div>
    </div>
  </section>

  <section class="sign sign--dark">
    <div class="dark-field"></div>
    <h2 class="headline headline--caps"><span class="line-1">OPEN</span><span class="line-2">HOUSE</span></h2>
    <div class="band"></div>
    <div class="brand"><span class="brand-name">LUMWICK</span><span class="brand-tag">REAL ESTATE</span></div>
    <div class="portrait" role="img" aria-label="Portrait photo of the agent"></div>
    <div class="contact">
      <div class="contact-row phone">
        <svg width="26" height="26" viewBox="0 0 26 26" aria-hidden="true"><circle cx="13" cy="13" r="13" fill="var(--brand-blue)"/><path d="M11 6c-2 1-3 3-3 7s1 6 3 7l2-3-2-2c-.4-1-.4-3 0-4l2-2z" fill="#fff"/></svg>
        <span>555-374-9126</span>
      </div>
      <div class="contact-row web">
        <svg width="24" height="22" viewBox="0 0 24 22" aria-hidden="true"><g fill="none" stroke="var(--brand-blue)" stroke-width="1.6"><circle cx="10" cy="10" r="8.5"/><ellipse cx="10" cy="10" rx="3.8" ry="8.5"/><path d="M1.5 10h17M3 5.5h14M3 14.5h14"/></g><path d="M15 13l7 3-3 1 2 3-1.5 1-2-3-2 2z" fill="var(--brand-blue)"/></svg>
        <span>www.lumwick-realestate.com</span>
      </div>
    </div>
  </section>

  <p class="label" style="left:79px; top:577px;">SAMPLE 1</p>
  <p class="label" style="left:561px; top:577px;">SAMPLE 2</p>
  <p class="label" style="left:79px; top:1147px;">SAMPLE 3</p>
  <p class="label" style="left:561px; top:1147px;">SAMPLE 4</p>

</body>
</html>
```